Business Card Design Project

I have attached the logo and the colour pallete for the branding for the company.

Creative designs for business cards are needed.

The Company is modern corporate.

Industry/Entity Type

Business

```html
<!DOCTYPE html>
<html lang="en">
<head>
<meta charset="utf-8">
<title>wayvia business card</title>
<link rel="stylesheet" href="https://fonts.googleapis.com/css2?family=Open+Sans:wght@400;600;700&display=swap">
<style>
  :root {
    --page-bg: #ece9e6;
    --card-white: #ffffff;
    --brand-purple: #8a3d94;
    --brand-purple-deep: #6a2a78;
    --brand-orange: #ee6444;
    --brand-orange-light: #f79a78;
    --text-dark: #2b2b2b;
  }
  html, body {
    margin: 0;
    padding: 0;
    width: 1200px;
    height: 990px;
    overflow: hidden;
    background: var(--page-bg);
    font-family: "Open Sans", Arial, sans-serif;
  }
  .canvas {
    position: relative;
    width: 1200px;
    height: 990px;
  }
  .card {
    position: absolute;
    width: 560px;
    height: 330px;
    background: var(--card-white);
    box-shadow: 0 6px 18px rgba(0,0,0,0.18);
    overflow: hidden;
  }
  .card-front { left: 90px; top: 150px; }
  .card-back  { left: 550px; top: 510px; }
  .card-art {
    position: absolute;
    inset: 0;
    width: 100%;
    height: 100%;
  }
  .brand-name {
    position: absolute;
    display: flex;
    align-items: center;
    gap: 10px;
    color: var(--brand-purple);
    font-weight: 600;
    letter-spacing: 1px;
    line-height: 1;
  }
  .brand-dot {
    display: inline-block;
    border-radius: 50%;
    background: var(--brand-orange);
  }
  .card-front .brand-name {
    left: 70px;
    top: 100px;
    font-size: 68px;
  }
  .card-front .brand-dot { width: 18px; height: 18px; }
  .card-back .brand-name {
    right: 36px;
    top: 34px;
    font-size: 30px;
    gap: 6px;
  }
  .card-back .brand-dot { width: 9px; height: 9px; }
  .contact {
    position: absolute;
    left: 62px;
    top: 68px;
    color: var(--text-dark);
  }
  .contact-company {
    margin: 0 0 6px;
    font-size: 21px;
    font-weight: 700;
  }
  .contact-list {
    list-style: none;
    margin: 0;
    padding: 0;
    font-size: 15px;
    line-height: 22px;
  }
</style>
</head>
<body>
<main class="canvas">

  <section class="card card-front" aria-label="Business card front">
    <svg class="card-art" viewBox="0 0 560 330" preserveAspectRatio="none" aria-hidden="true">
      <path d="M0 95 C 40 230, 200 300, 560 330 L 0 330 Z" fill="var(--brand-purple)"/>
      <path d="M0 150 C 60 260, 220 310, 420 330 L 0 330 Z" fill="var(--brand-purple-deep)" opacity="0.35"/>
      <path d="M140 230 C 260 190, 430 200, 560 250 L 560 330 L 420 330 C 330 290, 240 250, 140 230 Z" fill="var(--brand-orange)"/>
      <path d="M140 230 C 260 190, 430 200, 560 250 L 560 262 C 430 214, 270 206, 140 230 Z" fill="var(--brand-orange-light)"/>
    </svg>
    <div class="brand-name"><span>wayvia</span><span class="brand-dot"></span></div>
  </section>

  <section class="card card-back" aria-label="Business card back">
    <svg class="card-art" viewBox="0 0 560 330" preserveAspectRatio="none" aria-hidden="true">
      <path d="M0 190 C 30 260, 110 300, 230 330 L 0 330 Z" fill="var(--brand-purple)"/>
      <path d="M70 205 C 150 300, 330 300, 560 250 L 560 330 L 230 330 C 160 300, 100 260, 70 205 Z" fill="var(--brand-orange)"/>
      <path d="M70 205 C 150 286, 330 288, 560 238 L 560 250 C 330 300, 150 300, 70 205 Z" fill="var(--brand-orange-light)"/>
    </svg>
    <div class="brand-name"><span>wayvia</span><span class="brand-dot"></span></div>
    <div class="contact">
      <p class="contact-company">Company Name</p>
      <ul class="contact-list">
        <li>Phone: xxxxxxxxx</li>
        <li>Email: xxxxxxxxx</li>
        <li>Web: xxxxxxxxxxx</li>
      </ul>
    </div>
  </section>

</main>
</body>
</html>
```